New Branding Logo and Stationery Design Project

We are looking for a Stationary design for a company called "Peak Rebuilders". We are a Personal Training business that helps people of diverse ages, fitness levels and goals achieve what they aspire to. We are excellent at what we do and have a high rate of results. We are highly compassionate and love helping people. We want this to show in our logo. The logo must be able to be used on websites but also allow for large printing in the future also.

On the Business Card
Front we need the logo, and underneath this the words "Your health and fitness specialists".
On the back of the card we need:
Name (this will be different on the 2 peoples cards)
Health and fitness specialist
mobile: 04XX-XXX-XXX (we will give to the winner to add)
website: www.peakrebuilders.com.au
email: info@peakrebuilders.com.au
Down the bottom of the card we need a section that says something like:
"Your next appointment date is / / time : "

On the letterhead we will need:
Logo
Peak Rebuilders Pty Ltd
Address
Phone number
Email
Website

Target Market(s)

Anyone, any age who needs help with health and fitness

Industry/Entity Type

Printing

Requirements
Must have
• Templates for business cards here:
https://www.inkmarlow.com.au/businesscards_diy.php
Should not have
• Should not be Racist, Sexist, Ageist

```html
<!DOCTYPE html>
<html lang="en">
<head>
<meta charset="UTF-8">
<title>Peak Rebuilders – Business Cards</title>
<link href="https://fonts.googleapis.com/css2?family=Mulish:wght@400;600;800&display=swap" rel="stylesheet">
<style>
  :root{
    --stage:#2b2c2e;
    --paper:#f3f3f1;
    --brand-deep:#0d5a80;
    --brand-bright:#2a8cb6;
    --band:#1b7fa8;
    --ink-soft:#8a8d90;
    --ink-mid:#4a4d50;
  }
  *{margin:0;padding:0;box-sizing:border-box}
  html,body{width:1200px;height:800px;overflow:hidden;background:var(--stage);font-family:"Mulish",sans-serif}
  .stage{width:1200px;height:800px;display:flex;justify-content:center;align-items:center;gap:70px}
  .card{width:340px;height:560px;background:var(--paper);position:relative;overflow:hidden;box-shadow:0 12px 30px rgba(0,0,0,.45)}
  .brand{display:flex;align-items:center;gap:14px;padding:44px 30px 0}
  .brand-mark{width:26px;height:26px;background:var(--brand-bright);flex:none}
  .brand-name{font-weight:800;font-size:38px;line-height:1.02;color:var(--brand-deep);letter-spacing:.5px;text-transform:uppercase}
  .web{margin:26px 30px 0;font-size:18px;color:var(--brand-deep);text-align:right}
  .person{position:absolute;left:30px;right:30px;top:330px;text-align:center}
  .person-name{font-weight:800;font-size:22px;color:var(--brand-deep);letter-spacing:.5px;text-transform:uppercase}
  .person-role{font-size:18px;color:var(--brand-bright);margin-top:4px}
  .contact-band{position:absolute;left:0;right:0;bottom:0;height:140px;background:var(--band);color:#fff;padding:34px 30px 0;text-align:right;font-size:16px;line-height:1.7}
  .contact-band b{font-weight:800}
  .tagline{margin:36px 30px 0;text-align:center;font-weight:800;font-size:20px;line-height:1.25;color:var(--brand-deep);text-transform:uppercase}
  .appointments{margin:26px 34px 0;color:var(--ink-mid)}
  .appointments h2{font-weight:600;font-size:17px;text-align:center;margin-bottom:14px}
  .appointments ol{list-style:none}
  .appointments li{font-size:14px;color:var(--ink-soft);margin-bottom:16px;white-space:nowrap}
</style>
</head>
<body>
<main class="stage">
  <section class="card card-contact">
    <div class="brand"><span class="brand-mark"></span><span class="brand-name">Peak<br>Rebuilders</span></div>
    <p class="web">www.peakrebuilders.com.au</p>
    <div class="person">
      <p class="person-name">Liam Carter</p>
      <p class="person-role">Health and fitness specialist</p>
    </div>
    <div class="contact-band">
      <p><b>Mobile:</b> 0400-123-456</p>
      <p><b>Email:</b> info@peakrebuilders.com.au</p>
    </div>
  </section>

  <section class="card card-appointments">
    <div class="brand"><span class="brand-mark"></span><span class="brand-name">Peak<br>Rebuilders</span></div>
    <p class="tagline">Your health<br>and fitness specialists</p>
    <div class="appointments">
      <h2>Your Appointments</h2>
      <ol>
        <li>1. ___am/pm ______________ ___/___/___</li>
        <li>2. ___am/pm ______________ ___/___/___</li>
        <li>3. ___am/pm ______________ ___/___/___</li>
        <li>4. ___am/pm ______________ ___/___/___</li>
        <li>5. ___am/pm ______________ ___/___/___</li>
      </ol>
    </div>
  </section>
</main>
</body>
</html>
```